Web Design Project

need a website, logo and a matching business Card for design studio. i have a company that works with many companies and i want to offer design services that will be outsourced to craftflock.

this website is totally for the design services. i need it to be simple but very catcgy and trendy, yet MUST BE ELEGENT.

you being a designer will know best what do i require in this website and how it should look and feel..

i dont need many pages, most of the selling work to clients will be face to face, this is just for them to view the sample works.

the company is called "Corvelin, Vividra Studio", so pages i need are: 1- the Studio 2- Folios 3- Contact us( will include company informaiton, and online contact form that should have a drop-down list of all types of designs.

main focus is the folios pages, it needs to have samples of works, the classification of works should be on two basis, by type of design and by designer. client should be able to select a certain designer and send an inquiry. if the customer does that, then i should get all client details and the designer should get a notification that he has been requested though no contact details of client should be given to designer as i want to make sure that those jobs are given to designer through craft flock and this is an invitation for any designer who care to put his works on the website. next to that, if the customer requires a job online then we need to get information on how design should feel and look.

please quote your price to include the website and business card design, A3 head letter and envelope.

Please provide a mock up of your design or a briefing an initial design before asking to be announced as the winner.

my customers are general managers and decision makers.

Business

• ability to filiter works based on type or designer. and website must offer all types of designs included here

```html
<!DOCTYPE html>
<html lang="en">
<head>
<meta charset="utf-8">
<title>Corvelin, Vividra Studio</title>
<link href="https://fonts.googleapis.com/css2?family=Noto+Sans:wght@400;700&family=Shadows+Into+Light&display=swap" rel="stylesheet">
<style>
  :root {
    --page-top: #ecebe8;
    --page-bottom: #ffffff;
    --brand-blue: #2d54a8;
    --nav-text: #1c2f6e;
    --green-light: #a6d82a;
    --green-dark: #6fae0c;
    --card-border: #e4e4e4;
    --card-title: #777777;
    --arrow-blue: #1ea0e0;
    --arrow-blue-dark: #0c6fae;
    --footer-bg: #333a09;
    --footer-text: #f2f2e6;
    --link-blue: #2a86c9;
  }
  * { margin: 0; padding: 0; box-sizing: border-box; }
  html, body { width: 1200px; height: 1009px; overflow: hidden; }
  body {
    position: relative;
    font-family: "Noto Sans", sans-serif;
    background: linear-gradient(to bottom, var(--page-top) 0, var(--page-bottom) 170px, var(--page-bottom) 100%);
  }
  .brand {
    position: absolute; left: 112px; top: 24px;
    display: flex; align-items: center; gap: 14px;
    color: var(--brand-blue); font-weight: 700;
  }
  .brand-dot { width: 22px; height: 22px; border-radius: 50%; background: var(--green-light); }
  .brand-name { font-size: 46px; line-height: 1; letter-spacing: -0.5px; }
  .brand-name small { display: block; font-size: 24px; margin-top: 4px; margin-left: 60px; }

  .main-nav a {
    position: absolute; top: 98px; font-size: 19px; color: var(--nav-text); text-decoration: none;
  }
  .nav-home {
    left: 711px; width: 107px; height: 43px; top: 93px !important;
    line-height: 41px; text-align: center; color: #fff !important;
    border-radius: 5px;
    background: linear-gradient(var(--green-light), var(--green-dark));
  }
  .nav-home::after {
    content: ""; position: absolute; left: 34px; bottom: -11px;
    border-left: 0 solid transparent; border-right: 16px solid transparent;
    border-top: 12px solid var(--green-dark);
  }
  .nav-portfolio { left: 875px; top: 101px !important; }
  .nav-contact { left: 1031px; top: 101px !important; }

  .hero {
    position: absolute; left: 82px; top: 159px; width: 1049px; height: 354px;
    box-shadow: 0 18px 22px -14px rgba(0,0,0,0.28);
  }
  .hero-art {
    width: 100%; height: 100%;
    background:
      radial-gradient(ellipse 40% 60% at 20% 60%, rgba(180,255,210,0.55), transparent 70%),
      radial-gradient(ellipse 35% 55% at 55% 55%, rgba(255,240,80,0.75), transparent 70%),
      radial-gradient(ellipse 30% 50% at 92% 80%, rgba(240,120,30,0.8), transparent 70%),
      linear-gradient(100deg, #33b58a 0%, #9fd33a 25%, #e2d62a 48%, #6b5a10 72%, #1a1208 88%, #a04d10 100%);
  }
  .hero-title {
    position: absolute; right: 68px; top: 68px;
    font-family: "Shadows Into Light", cursive; font-size: 58px; color: #fff; letter-spacing: 1px;
  }
  .hero-arrow {
    position: absolute; top: 308px; width: 58px; height: 69px; border-radius: 6px;
    background: linear-gradient(var(--arrow-blue), var(--arrow-blue-dark));
    box-shadow: 0 3px 4px rgba(0,0,0,0.3);
  }
  .hero-arrow svg { position: absolute; left: 13px; top: 16px; }
  .hero-prev { left: 70px; }
  .hero-next { left: 1086px; }

  .divider {
    position: absolute; left: 40px; width: 1120px; height: 2px;
    background: linear-gradient(to right, transparent, #dcdcdc 15%, #dcdcdc 85%, transparent);
  }
  .divider-top { top: 570px; }
  .divider-bottom { top: 838px; }

  .service-card {
    position: absolute; top: 600px; width: 163px; height: 200px;
    border: 2px solid var(--card-border); border-radius: 8px; background: #fff; text-align: center;
  }
  .service-title { margin-top: 13px; font-size: 17px; font-weight: 700; color: var(--card-title); }
  .service-icon {
    width: 84px; height: 84px; margin: 18px auto 0; border-radius: 12px;
  }
  .service-btn {
    position: absolute; left: 29px; top: 157px; width: 104px; height: 24px; border-radius: 12px;
    background: linear-gradient(#b9e558, #6fb415); border: 1px solid #5d9a10;
    font-size: 12px; line-height: 22px; color: #1d2a05;
  }
  .icon-web { background: radial-gradient(circle at 45% 40%, #6aa8f0, #1c4fb0 70%); border-radius: 50%; width: 70px; height: 70px; margin-top: 24px; }
  .icon-card { background: linear-gradient(#d6e6f6, #8fb3d6); height: 60px; margin-top: 30px; }
  .icon-adv { background: linear-gradient(#d43b2a, #7e1f15); }
  .icon-logo { background: linear-gradient(#e2e2e2, #9a9a9a); }
  .icon-shirt { background: linear-gradient(#f8f08a, #e0d64a); }

  .carousel-arrow {
    position: absolute; top: 670px; width: 46px; height: 60px; border-radius: 50%;
    background: radial-gradient(circle at 50% 50%, #fafafa, #d9d9d9);
  }
  .carousel-arrow svg { position: absolute; left: 17px; top: 23px; }
  .carousel-prev { left: 76px; }
  .carousel-next { left: 1092px; }

  .see-all {
    position: absolute; left: 1050px; top: 860px; display: flex; align-items: center; gap: 6px;
    font-size: 12px; color: var(--link-blue); text-decoration: underline;
  }

  .site-footer {
    position: absolute; left: 70px; top: 921px; width: 1072px; height: 79px;
    background: var(--footer-bg); border-top: 2px solid #4d6fa0; color: var(--footer-text); font-size: 11px;
  }
  .newsletter-label { position: absolute; left: 12px; top: 15px; }
  .newsletter-input {
    position: absolute; left: 12px; top: 36px; width: 186px; height: 25px; background: #fff;
    color: #8a8a8a; font-size: 11px; line-height: 25px; padding-left: 6px;
  }
  .newsletter-go {
    position: absolute; right: 3px; top: 4px; width: 17px; height: 17px; background: #222;
  }
  .newsletter-go svg { position: absolute; left: 5px; top: 4px; }
  .social-label { position: absolute; left: 252px; top: 15px; }
  .social-box { position: absolute; top: 42px; width: 17px; height: 17px; background: #1b1f04; border: 1px solid #555c2a; }
  .social-one { left: 253px; }
  .social-two { left: 277px; }
  .footer-links, .footer-legal { position: absolute; right: 14px; text-align: right; }
  .footer-links { top: 18px; }
  .footer-legal { top: 35px; }
  .sep { margin: 0 9px; }
</style>
</head>
<body>
  <header>
    <div class="brand">
      <span class="brand-dot"></span>
      <div class="brand-name">Corvelin<small>Vividra Studio</small></div>
    </div>
    <nav class="main-nav">
      <a class="nav-home" href="#">Home</a>
      <a class="nav-portfolio" href="#">Portfolio</a>
      <a class="nav-contact" href="#">Contact</a>
    </nav>
  </header>

  <section class="hero">
    <div class="hero-art" role="img" aria-label="Glowing bokeh light circles and flowing curves in green, yellow and orange"></div>
    <h1 class="hero-title">Personify Your Business</h1>
  </section>
  <div class="hero-arrow hero-prev"><svg width="30" height="36" viewBox="0 0 30 36"><polygon points="26,3 4,18 26,33" fill="#0a4e82"/></svg></div>
  <div class="hero-arrow hero-next"><svg width="30" height="36" viewBox="0 0 30 36"><polygon points="4,3 26,18 4,33" fill="#0a4e82"/></svg></div>

  <div class="divider divider-top"></div>

  <div class="carousel-arrow carousel-prev"><svg width="10" height="14" viewBox="0 0 10 14"><polyline points="8,1 2,7 8,13" fill="none" stroke="#8b5a66" stroke-width="3"/></svg></div>
  <article class="service-card" style="left:151px">
    <h2 class="service-title">Web Design</h2>
    <div class="service-icon icon-web" role="img" aria-label="Globe with a pen icon"></div>
    <div class="service-btn">View Portfolio</div>
  </article>
  <article class="service-card" style="left:337px">
    <h2 class="service-title">Business Card</h2>
    <div class="service-icon icon-card" role="img" aria-label="Contact card icon"></div>
    <div class="service-btn">View Portfolio</div>
  </article>
  <article class="service-card" style="left:525px">
    <h2 class="service-title">Adv. Design</h2>
    <div class="service-icon icon-adv" role="img" aria-label="Billboard being painted icon"></div>
    <div class="service-btn">View Portfolio</div>
  </article>
  <article class="service-card" style="left:711px">
    <h2 class="service-title">Logo Design</h2>
    <div class="service-icon icon-logo" role="img" aria-label="Cup of paint brushes icon"></div>
    <div class="service-btn">View Portfolio</div>
  </article>
  <article class="service-card" style="left:898px">
    <h2 class="service-title">Web Design</h2>
    <div class="service-icon icon-shirt" role="img" aria-label="Printed T-shirt icon"></div>
    <div class="service-btn">View Portfolio</div>
  </article>
  <div class="carousel-arrow carousel-next"><svg width="10" height="14" viewBox="0 0 10 14"><polyline points="2,1 8,7 2,13" fill="none" stroke="#8b5a66" stroke-width="3"/></svg></div>

  <div class="divider divider-bottom"></div>

  <a class="see-all" href="#">
    <svg width="20" height="20" viewBox="0 0 20 20"><circle cx="10" cy="10" r="9" fill="#fff" stroke="#b8b8b8"/><polygon points="8,5 14,10 8,15" fill="#1f6fb0"/></svg>
    See All
  </a>

  <footer class="site-footer">
    <div class="newsletter-label">Get Recent Updates and offers</div>
    <div class="newsletter-input">type your email here
      <span class="newsletter-go"><svg width="8" height="9" viewBox="0 0 8 9"><polyline points="1,0.5 6,4.5 1,8.5" fill="none" stroke="#fff" stroke-width="2"/></svg></span>
    </div>
    <div class="social-label">Get in touch with us</div>
    <span class="social-box social-one"></span>
    <span class="social-box social-two"></span>
    <div class="footer-links">Home<span class="sep">|</span>Portfolio<span class="sep">|</span>Contact</div>
    <div class="footer-legal">© 2012, All rights Reserved<span class="sep">|</span>Privacy Policy<span class="sep">|</span>Terms &amp; Conditions</div>
  </footer>
</body>
</html>
```